Info flyer to showcase security camera install and remote video monitoring.

I am looking for an attractive looking flyer that is simple and has some text content and some photos to show prospective clients what services I can provide them.

The two main services that I want to showcase are:
1. Security Camera & NVR Installations and maintenance
2. Remote Video Monitoring for business. This can be a temporary service or ongoing/long term.

Target Market(s)

Construction, Retail, Industrial, Commercial

Industry/Entity Type

Security

Font styles to use
Serif

Colors

Designer to choose colors to be used in the design.

```html
<!DOCTYPE html>
<html lang="en">
<head>
<meta charset="utf-8">
<title>Vantage Secure Systems – Services Flyer</title>
<link rel="stylesheet" href="https://fonts.googleapis.com/css2?family=Kanit:wght@500;600&family=Mada:wght@400;700&display=swap">
<style>
  :root {
    --gold: #c99b2d;
    --gold-soft: #ead9b0;
    --ink: #1e1c1c;
    --paper: #ffffff;
    --grey: #b9b9b9;
    --grey-dark: #555555;
    --sky-top: #2c79c4;
    --sky-bottom: #3d8ad2;
    --mall-a: #c9ccd0;
    --mall-b: #5d6b86;
  }
  * { margin: 0; padding: 0; box-sizing: border-box; }
  html, body { width: 714px; height: 1200px; overflow: hidden; background: var(--paper); }
  body { font-family: "Mada", Arial, sans-serif; color: var(--ink); }
  .flyer { position: relative; width: 714px; height: 1200px; background: var(--paper); overflow: hidden; }

  .brand { position: absolute; top: 58px; left: 0; width: 100%; display: flex; justify-content: center; align-items: center; gap: 14px; }
  .brand-mark { width: 40px; height: 40px; border-radius: 50%; background: var(--ink); flex: none; }
  .brand-name { font-family: "Kanit", Arial, sans-serif; font-weight: 600; font-size: 44px; line-height: 1; letter-spacing: 0.5px; color: var(--ink); }
  .brand-name small { display: block; font-size: 18px; letter-spacing: 0.6px; margin-top: 4px; }

  .hero-band { position: absolute; top: 191px; left: 0; width: 714px; height: 457px; background: var(--gold); }
  .hero-art { position: absolute; top: 0; left: 0; }

  .services-title { position: absolute; top: 706px; left: 38px; font-family: "Kanit", Arial, sans-serif; font-weight: 500; font-size: 42px; letter-spacing: 0.5px; color: var(--ink); }
  .services-title span { color: var(--gold); }

  .service { position: absolute; left: 0; width: 560px; }
  .service-num { position: absolute; left: 33px; width: 52px; height: 52px; border-radius: 50%; background: var(--grey); border: 2px solid #9d9d9d; display: flex; align-items: center; justify-content: center; font-family: "Kanit", Arial, sans-serif; font-size: 28px; color: var(--ink); }
  .service-text { position: absolute; left: 125px; font-size: 24px; line-height: 38px; color: var(--ink); white-space: nowrap; }
  .service-text b { font-weight: 700; }
  .service--install { top: 820px; }
  .service--install .service-num { top: 34px; }
  .service--monitor { top: 978px; }
  .service--monitor .service-num { top: 39px; }

  .quote { position: absolute; font-family: Georgia, serif; font-size: 130px; line-height: 1; color: var(--gold-soft); }
  .quote--open { top: 800px; left: 70px; }
  .quote--close { top: 1080px; left: 345px; }

  .contact { position: absolute; top: 1030px; left: 460px; width: 240px; text-align: center; }
  .contact-phone { font-size: 27px; letter-spacing: 1px; margin-top: 10px; color: var(--ink); }
  .contact-web { font-size: 13px; color: var(--ink); }
</style>
</head>
<body>
<main class="flyer">
  <header class="brand">
    <span class="brand-mark"></span>
    <span class="brand-name">VANTAGE<small>SECURE SYSTEMS</small></span>
  </header>

  <div class="hero-band"></div>

  <svg class="hero-art" width="714" height="1200" viewBox="0 0 714 1200">
    <defs>
      <radialGradient id="mallTones" cx="50%" cy="45%" r="60%">
        <stop offset="0%" stop-color="var(--mall-a)"/>
        <stop offset="100%" stop-color="var(--mall-b)"/>
      </radialGradient>
      <linearGradient id="skyTones" x1="0" y1="0" x2="0" y2="1">
        <stop offset="0%" stop-color="var(--sky-top)"/>
        <stop offset="100%" stop-color="var(--sky-bottom)"/>
      </linearGradient>
    </defs>
    <g fill="none" stroke="var(--gold-soft)" stroke-width="1">
      <circle cx="360" cy="430" r="270"/>
      <circle cx="546" cy="688" r="175"/>
      <circle cx="546" cy="688" r="190"/>
    </g>
    <circle cx="360" cy="430" r="240" fill="var(--ink)"/>
    <circle cx="382" cy="430" r="208" fill="url(#mallTones)" role="img" aria-label="Photo: dome security camera hanging in a busy shopping mall"/>
    <circle cx="546" cy="688" r="152" fill="var(--paper)"/>
    <circle cx="546" cy="688" r="142" fill="var(--ink)"/>
    <circle cx="546" cy="688" r="124" fill="url(#skyTones)" role="img" aria-label="Photo: security cameras mounted on a pole against blue sky"/>
  </svg>

  <h2 class="services-title">OUR <span>SERVICES:</span></h2>

  <div class="quote quote--open">&ldquo;</div>

  <section class="service service--install">
    <div class="service-num">1</div>
    <p class="service-text"><b>Security Camera</b> &amp;<br><b>NVR Installations</b><br>and <b>maintenance</b></p>
  </section>

  <section class="service service--monitor">
    <div class="service-num">2</div>
    <p class="service-text"><b>Remote Video Monitoring</b><br>for business. This can be a<br>temporary service or<br>ongoing/long term.</p>
  </section>

  <div class="quote quote--close">&rdquo;</div>

  <aside class="contact">
    <svg width="44" height="34" viewBox="0 0 44 34" aria-hidden="true">
      <path d="M2 12 Q22 -2 42 12 L38 17 L30 14 L30 9 Q22 6 14 9 L14 14 L6 17 Z" fill="var(--gold)"/>
      <path d="M12 16 L32 16 L39 32 L5 32 Z" fill="var(--gold)"/>
      <circle cx="22" cy="24" r="5" fill="var(--paper)"/>
      <circle cx="22" cy="24" r="2" fill="var(--gold)"/>
    </svg>
    <p class="contact-phone">555-014-2090</p>
    <p class="contact-web">www.vantagesecure.com</p>
  </aside>
</main>
</body>
</html>
```